Flyer Design Project

I need a flyer designed for my new dog grooming business.
I have just ordered fridge magnet business cards and would like a flyer to send them out with, if you could create a flyer and put some ideas together using the information provided to help promote my business.
The business is called Tallowby Pawcare,
I groom small dogs.
I’d like to have on the flyer the services I offer,
One on one quality care for the customers pet,
Full dog grooms, clipper clips, scissor snips and full shaves,
Sanitary clips, nails clipped, DE shedding,
Various brushing styles and techniques,
All professional equipment and products used,
Medicated shampoos & groomers fluffana wash & colognes,
Hydro dog bath and heater blow dryer.
My profession also id like to have on the flyer:
(A certified pet hygienist & dog Groomer)
I’d like the Tallowby Pawcare logo with the purple paw prints in the writing on the flyer ( will upload pic of logo)
I’d also like the website displayed the email and the phone number all clearly on the flyer also thank you.
Website address: tallowbypawcare.com.au
Email address: info@tallowbypawcare.com.au
Phone number: 0412 580 264
When this flyer has finally been created & finalised, I will need to have sent to me all raw formats and fonts i.e. vector files to be able to provide my sign writer to make the grey in my logo foil instead of silver. Thankyou

regarding size of the flyer i would like the flyer to be size A5 (210mm x 148mm) thankyou.

also when adding dogs to the flyer try sick to the smaller breeds all the flyers look great so far

can i also please have the website,phone number and email writting big or bold on the flyer to stand out.
thankyou
Updates

the text medicated shampoos, groomers fluffana was & colones are now to be changed to

(medicated shampoo's, groomers fluffana & scented colones)

and one on one quality care for the customers pet changed to

(one on one quality care for your pet)

Target Market(s)

dog owners

Industry/Entity Type

Pet

Requirements
Should not have
• no pricings included or any special deals

```html
<!DOCTYPE html>
<html lang="en">
<head>
<meta charset="utf-8">
<title>Tallowby Pawcare – A5 Flyer, Back and Front</title>
<link rel="stylesheet" href="https://fonts.googleapis.com/css2?family=Berkshire+Swash&family=Fredoka:wght@600&display=swap">
<style>
  :root{
    --board:#000;
    --paper:#fff;
    --ink:#111;
    --cyan:#27b9ea;
    --purple:#bf4c9f;
    --plum:#8e3b91;
    --grey:#cfcfcf;
    --logo-box:#161616;
    --script:"Berkshire Swash", cursive;
    --rounded:"Fredoka", sans-serif;
    --body:Arial, Helvetica, sans-serif;
  }
  *{box-sizing:border-box;margin:0;padding:0}
  html,body{width:1200px;height:849px;overflow:hidden;background:var(--board)}
  .board{position:relative;width:1300px;height:920px;transform:scale(0.92308);transform-origin:0 0;background:var(--board)}
  .side-label{position:absolute;top:24px;color:#fff;font:15px var(--body);transform:translateX(-50%)}
  .flyer{position:absolute;top:64px;width:560px;height:795px;background:var(--paper);overflow:hidden}
  .flyer--back{left:53px}
  .flyer--front{left:664px}
  .flyer svg.decor{position:absolute;inset:0;width:100%;height:100%}
  .photo{position:absolute}
  .logo-box{position:absolute;background:var(--logo-box);display:flex;flex-direction:column;align-items:center;justify-content:center}
  .brand-name{font:600 46px var(--rounded);color:var(--grey);line-height:1;white-space:nowrap}
  .tagline{margin-top:18px;font:13px var(--body);letter-spacing:4.6px;color:#777}
  .headline{position:absolute;font-family:var(--script);line-height:1}
  .headline .line-1{display:block;color:var(--cyan);font-size:42px}
  .headline .line-2{display:block;color:var(--purple);font-size:50px;margin-top:6px;margin-left:2px}
  .contact-card{position:absolute;left:140px;top:598px;width:296px;height:168px;background:#050505;border-radius:9px;text-align:center;padding-top:6px}
  .contact-card .card-url{font:600 22px var(--rounded);color:var(--cyan)}
  .contact-card .brand-name{font-size:36px;margin-top:20px;display:block}
  .contact-card .card-phone{font:600 24px var(--rounded);color:var(--grey);margin-top:16px}
  .contact-card .card-email{font:600 12px var(--rounded);color:var(--cyan);margin-top:2px}
  .services-title{position:absolute;left:32px;top:196px;font:40px var(--script);color:var(--cyan)}
  .services-list{position:absolute;left:33px;top:245px;width:330px;font:15px/19.4px var(--body);color:var(--ink);list-style:none}
  .services-list li{position:relative;padding-left:24px}
  .services-list li::before{content:"•";position:absolute;left:0}
  .front-contact{position:absolute;right:30px;font-family:var(--script);color:var(--ink);white-space:nowrap}
  .front-phone{top:706px;font-size:37px}
  .front-url{top:752px;font-size:30px;font-weight:bold}
</style>
</head>
<body>
<main class="board">
  <span class="side-label" style="left:320px">BACK</span>
  <span class="side-label" style="left:893px">FRONT</span>

  <!-- Back of flyer -->
  <section class="flyer flyer--back" aria-label="Flyer back">
    <svg class="decor" viewBox="0 0 560 795" aria-hidden="true">
      <path d="M9,6 H551 V190 C470,170 360,175 250,230 C160,275 80,300 9,295 Z" fill="#000"/>
      <path d="M9,295 C80,300 160,275 250,230 C360,175 470,170 551,190 V205 C470,190 370,198 270,248 C170,298 80,325 9,320 Z" fill="var(--cyan)"/>
      <g fill="var(--grey)">
        <circle cx="128" cy="275" r="26"/>
      </g>
      <path d="M50,90 C10,60 0,30 20,15 C40,0 50,20 50,30 C50,20 60,0 80,15 C100,30 90,60 50,90" transform="translate(360,125) scale(1.7,1.5)" fill="none" stroke="var(--purple)" stroke-width="6"/>
      <path d="M50,90 C10,60 0,30 20,15 C40,0 50,20 50,30 C50,20 60,0 80,15 C100,30 90,60 50,90" transform="translate(28,390) scale(0.85,0.85)" fill="none" stroke="var(--purple)" stroke-width="7"/>
    </svg>
    <div class="logo-box" style="left:34px;top:21px;width:356px;height:135px">
      <span class="brand-name">Tallowby Pawcare</span>
    </div>
    <h2 class="headline" style="left:296px;top:270px">
      <span class="line-1">Pamper your</span>
      <span class="line-2">best Friend</span>
    </h2>
    <div class="photo" role="img" aria-label="Group of small dog breeds sitting in a row" style="left:14px;top:346px;width:545px;height:236px;background:radial-gradient(ellipse at 55% 60%,#b98a5e 0%,#d9c2a6 45%,rgba(255,255,255,0) 75%)"></div>
    <div class="contact-card">
      <div class="card-url">tallowbypawcare.com.au</div>
      <span class="brand-name">Tallowby Pawcare</span>
      <div class="card-phone">0412 580 264</div>
      <div class="card-email">info@tallowbypawcare.com.au</div>
    </div>
  </section>

  <!-- Front of flyer -->
  <section class="flyer flyer--front" aria-label="Flyer front">
    <svg class="decor" viewBox="0 0 560 795" aria-hidden="true">
      <rect x="9" y="7" width="540" height="169" fill="#000"/>
      <path d="M0,478 C90,455 190,460 290,520 C390,580 470,598 560,588 V795 H0 Z" fill="var(--purple)"/>
      <path d="M0,512 C100,492 200,500 300,556 C400,612 480,612 560,596 V795 H0 Z" fill="var(--cyan)"/>
      <circle cx="372" cy="222" r="30" fill="var(--cyan)"/>
      <circle cx="240" cy="630" r="40" fill="#2b9cc3" opacity="0.6"/>
      <circle cx="78" cy="710" r="52" fill="var(--plum)"/>
      <path d="M50,90 C10,60 0,30 20,15 C40,0 50,20 50,30 C50,20 60,0 80,15 C100,30 90,60 50,90" transform="translate(424,212) scale(1.25,1.15)" fill="none" stroke="var(--purple)" stroke-width="6"/>
    </svg>
    <div class="logo-box" style="left:104px;top:18px;width:354px;height:138px">
      <span class="brand-name">Tallowby Pawcare</span>
      <span class="tagline">PAMPER YOUR BEST FRIEND</span>
    </div>
    <h2 class="services-title">Our Services</h2>
    <ul class="services-list">
      <li>Quality care for the customers pet,</li>
      <li>Full dog grooms, clipper clips, scissor snips and full shaves,</li>
      <li>Sanitary clips, nails clipped, DE shedding,</li>
      <li>Various brushing styles and techniques,</li>
      <li>All professional equipment and products used, Medicated shampoos &amp; groomers fluffana wash &amp; colognes,</li>
      <li>Hydro dog bath and heater blow dryer.</li>
    </ul>
    <div class="photo" role="img" aria-label="Pug sitting" style="left:50px;top:426px;width:122px;height:206px;background:radial-gradient(ellipse at 50% 55%,#d8c3a0 0%,#c9ad85 55%,rgba(255,255,255,0) 72%)"></div>
    <div class="photo" role="img" aria-label="West Highland white terrier sitting" style="left:346px;top:291px;width:208px;height:336px;background:radial-gradient(ellipse at 50% 50%,#efe9dc 0%,#e0d6c2 55%,rgba(255,255,255,0) 72%)"></div>
    <div class="front-contact front-phone">Phone : 0412 580 264</div>
    <div class="front-contact front-url">tallowbypawcare.com.au</div>
  </section>
</main>
</body>
</html>
```